Sticker Design

Wanting business name across the bottom of car doors, please see attached. looking for something simple and require asap. Happy for black and white simple colouring.

Thank you
Dane Morvill

```html
<!DOCTYPE html>
<html lang="en">
<head>
<meta charset="utf-8">
<title>NVR Field Service and Logistics – Door Sticker</title>
<link rel="stylesheet" href="https://fonts.googleapis.com/css2?family=Exo+2:wght@500;700;800&display=swap">
<style>
  :root {
    --sticker-black: #0d0d0d;
    --sticker-white: #ffffff;
    --stripe-tone-light: #d9d9d9;
    --stripe-tone-dark: #8a8a8a;
    --canvas-bg: #e9ebee;
  }
  html, body {
    margin: 0;
    padding: 0;
    width: 1200px;
    height: 454px;
    overflow: hidden;
    background: var(--canvas-bg);
  }
  .canvas {
    width: 1200px;
    height: 454px;
    display: flex;
    align-items: center;
    justify-content: center;
  }
  .door-sticker {
    width: 1160px;
    height: auto;
    display: block;
  }
  .sticker-band { fill: var(--sticker-black); }
  .stripe-area { fill: url(#stripeTone); }
  .accent-line { stroke: var(--sticker-white); stroke-width: 2.4; }
  .brand-name {
    font-family: "Exo 2", sans-serif;
    font-weight: 800;
    font-size: 30px;
    fill: var(--sticker-white);
  }
  .brand-mark { fill: none; stroke: var(--sticker-white); stroke-width: 3; }
  .tagline {
    font-family: "Exo 2", sans-serif;
    font-weight: 700;
    font-size: 15px;
    fill: var(--sticker-white);
  }
  .phone-number {
    font-family: "Exo 2", sans-serif;
    font-weight: 700;
    font-size: 19px;
    fill: var(--sticker-white);
  }
</style>
</head>
<body>
<main class="canvas">
  <svg class="door-sticker" viewBox="0 0 720 50" xmlns="http://www.w3.org/2000/svg" aria-label="NVR Field Service and Logistics door sticker">
    <defs>
      <linearGradient id="stripeTone" x1="0" y1="0" x2="1" y2="0">
        <stop offset="0" stop-color="var(--stripe-tone-light)"/>
        <stop offset="1" stop-color="var(--stripe-tone-dark)"/>
      </linearGradient>
    </defs>

    <polygon class="sticker-band" points="0,0 720,0 710,50 0,50"/>

    <rect class="stripe-area" x="6" y="10" width="146" height="32" role="img" aria-label="Decorative speed stripe graphic"/>

    <g class="brand">
      <text class="brand-name" x="183" y="37" textLength="70" lengthAdjust="spacingAndGlyphs">NVR</text>
      <circle class="brand-mark" cx="284" cy="26" r="12"/>
    </g>

    <text class="tagline" x="500" y="20" text-anchor="middle" textLength="326" lengthAdjust="spacing">FIELD SERVICE AND LOGISTICS</text>
    <line class="accent-line" x1="301" y1="40" x2="403" y2="40"/>
    <text class="phone-number" x="500" y="45" text-anchor="middle" textLength="178" lengthAdjust="spacing">0412555837</text>
    <line class="accent-line" x1="596" y1="40" x2="705" y2="40"/>
  </svg>
</main>
</body>
</html>
```